Fern Porter Website Professional and Crisp Redesign

Hi Teams,
Good evening! I am looking for a Warm Crisp and Professional redesign of my company's website at www.FernPorter-example.com. Please google "Valet Trash" also to see the low rent stuff my competition is doing. I have included so much material for you to help your creative minds collaborate with. We use Wordpress now and have a mobile app plug in that is using xmlrpc to communicate back and forth iOS and Android. Swift for iOS and Java for android. Wordpress for the site. Good Luck!
Heres a little test site we fooled around with http://fern.qlorvan.example to get ideas flowing, if needed.
Use the new content and redesign file for page content/copy. We all add information like Bio's when we get there.
I want you to be creative - use your own words, just be crisp about it.
Home Page:
Concept:
Nice marsh/tide/palm tree image of a community, poised up to the sky.
Fern porter sign for each of the respective redirections/pages. (4 total)
Statement:
Fern Porter is a leading valet trash and recycling service provider offering robust and flexible solutions for your community’s recycling, waste and maintenance needs. Connect with us and let us give you and your residents the experience they deserve: Better people, better processes, and better technologies.
Video –
Client Login – top left always
Slogan – Improve the day with valet.
Tabs: (Could be in boxes or the Fern Porter sign)
1. Residents
2. Property Management
3. About us
4. Contact
Residents Page:
Dear Resident,
Making sure that our environment and communities stay beautiful is a part of Fern Porter’s mission. We owe it to ourselves to be more thoughtful in our own waste production by ensuring the items we discard have fulfilled their highest and best uses. We are thankful for the steps we take together that propel us in the right direction.
Video.
Why Valet:
Fern Porter solves the embarrassment and effort of handling waste and recycling for the sophisticated multifamily resident. We always like to say – find us one person who likes to take out the trash…
Service guidelines on display and downloadable.
Oops!
Picture of an example oops note –
Get one of these?! No sweat, just correct the checked box the next night and we will happily take your trash/recycling the next scheduled service evening.
Essentials:
1. Trash is tied, bagged, and in the provided container.
(max 2 bags, 25 lbs/night)
2. Ensure bins are placed and returned at the agreed upon times.
3. Always feel free to contact us with any questions, comments, or concerns.
Management Page
Dear Management,
As our multifamily industry grows and continues to evolve with our residents, add value industries like Valet Trash are emerging as best bets for better serving your community as a whole. Knowing the industry as we do, Fern Porter knows that how we perform in New York, directly impacts our teams opportunities in Florida. By instilling this united culture we are consistently able to outperform our industry’s key performance indicators such as retention rate that affords Fern Porter the advantage in most cases.
Video:
Why Fern?
1. Our Values –
Integrity | We are transparent and forthright in what we do.
Outstanding Customer Service | For us this means doing more than just what we are compensated for.
Accountability | In our industry, it’s the one miss that is remembered, so we always have redundancy plans and the technology needed to keep our clients well rested.
Strong Work Ethic | Discipline is the cornerstone of great results, and reliability.
2. Our People –
Fern Porter hosts tryouts, not interviews for all its thoroughly background checked employees. Tryouts ensure our high standards of integrity, accountability, and strong work ethics are consistently observed before allowing them on-site alone.
3. Our Process –
Our employee’s are trained to be safe problem solvers from the start. We take a 500-foot view above the job scope to develop safer, more efficient, and through ways of improving our work and culture. Then, we listen.
4. Our Technology –
Technology has allowed Fern Porter to better bridge the communication gap for our clients to get on-site performance data real time. Our application, R4K (Route for keeps), allows fast accurate reporting of our job assignments. This tool takes out the guesswork and follow up time when we have inquires.
5. Our Dividends –
No need to budget when our service generates profit infinitely with no start up investment through our phase in programs. We will always consider buying out the current provider’s contract as requested.
6. Our Involvements –
A chief aim for Fern Porter is to uplift and connect with our teammates, our clients, and our communities. We always find brilliant ways to contribute both with micro and macro impacts consistently. Check the attendance records of your local and national meetings and events – you’ll see that we show up. We are committed.
Connect with us to inquire more information and pricing
Info@FernPorter-example.com | 885- FERN-KQS
Download information package
About
Hi There,
After spilling leaking trash in a brand new car on the way to the community compactor, enough was enough. The company was formed that same evening and the founder turned in his safe executive roll for a fortune 500 company and dove into the world of the unknown – Entrepreneurship. Through the merits of our service, self-investment, and teach-ability index Fern Porter is fast becoming a stable leader in setting the standard for valet trash.
Video
Leadership
Executive Team
Mel Garrick
Hal Venterman
Paula Renick
Lorna Quillet
Theresa Mulvane
Area Management
New York
South Carolina
North Carolina
Georgia
Florida
Louisiana
Alabama
Texas
Contact page:
Pretty straight forward.
Again Good Luck!
Mel Garrick
President
Fern Porter
Target Market(s)
Professionals
Industry/Entity Type
Apartment
Number of Pages Required
5+ page
Font styles to use
Requirements
Must have
- Professional, Organized, and Crisp
Nice to have
- You go out on your own and put your own touch on it. That would be refreshing.
Should not have
- Don't use the word "Complex" to talk about apartments. Have fun!

```html
<!DOCTYPE html>
<html lang="en">
<head>
<meta charset="utf-8">
<title>Fern Porter – Home</title>
<link href="https://fonts.googleapis.com/css2?family=Mulish:wght@400;600;700&family=Open+Sans:wght@400;600&display=swap" rel="stylesheet">
<style>
:root{
  --navy:#1f2f6b;
  --brand:#2f6fb8;
  --sky:#7fc3e6;
  --sky-line:#5aaee0;
  --grey-text:#6d6d6d;
  --dark:#222;
  --footer:#82a9d4;
  --footer-bottom:#b9cfe7;
  --topbar:#f1f1f1;
  --login:#7ea8d6;
}
*{box-sizing:border-box;margin:0;padding:0}
html,body{width:1200px;height:2350px;overflow:hidden;background:#fff}
body{font-family:"Open Sans",Arial,sans-serif;color:var(--dark);position:relative}
.abs{position:absolute}
.topbar{left:0;top:0;width:1200px;height:38px;background:var(--topbar)}
.client-login{left:121px;top:0;width:125px;height:38px;background:var(--login);color:#fff;font:400 15px "Mulish",sans-serif;display:flex;align-items:center;justify-content:center}
.social{left:951px;top:5px;display:flex;gap:5px}
.social span{width:27px;height:27px;border:2px solid var(--navy);border-radius:50%;display:block}
.header{left:0;top:38px;width:1200px;height:119px;background:#fff}
.brand{left:117px;top:60px;display:flex;align-items:center;gap:10px}
.brand-dot{width:64px;height:64px;border:5px solid var(--brand);border-radius:50%}
.brand-name{font:700 34px/1 "Mulish",sans-serif;color:var(--brand)}
.brand-phone{font:400 16px "Mulish",sans-serif;color:var(--navy);margin-top:6px}
.nav a{position:absolute;top:86px;font:400 18px "Mulish",sans-serif;color:#8a8a8a;text-decoration:none}
.nav a.active{color:var(--navy);font-weight:600}
.nav-underline{left:440px;top:152px;width:65px;height:5px;background:var(--navy)}
.hero{left:0;top:157px;width:1200px;height:573px;background:linear-gradient(180deg,#a9a8b8 0%,#8d93a0 12%,#6f8a5a 28%,#5f8341 50%,#6d8a45 72%,#9c8790 90%,#8b7a72 100%)}
.hero-title{left:0;top:312px;width:1200px;text-align:center;font:600 49px "Mulish",sans-serif;color:#fff}
.hero-sub{left:0;top:382px;width:1200px;text-align:center;font:400 25px "Mulish",sans-serif;color:#fff}
.hero-btn{left:519px;top:437px;width:164px;height:41px;border:2px solid #fff;color:#fff;font:400 17px "Mulish",sans-serif;display:flex;align-items:center;justify-content:center}
.dots{left:517px;top:689px;display:flex;gap:7px}
.dots span{width:33px;height:3px;background:#fff;display:block}
.dots span.on{background:var(--sky-line)}
.section-title{left:0;width:1200px;text-align:center;font:400 33px "Mulish",sans-serif}
.title-rule{left:569px;width:62px;height:3px;background:var(--sky-line)}
.welcome-title{top:797px;color:var(--navy)}
.intro{left:230px;top:866px;width:740px;text-align:center;font:400 16px/24px "Open Sans",sans-serif;color:var(--grey-text)}
.intro p+p{margin-top:13px}
.btn-fill{left:522px;top:1003px;width:161px;height:42px;background:var(--sky);color:#fff;font:600 15px "Mulish",sans-serif;display:flex;align-items:center;justify-content:center;letter-spacing:.5px}
.divider{left:130px;top:1089px;width:942px;height:1px;background:#ddd}
.video-title{top:1113px;color:#111;font-size:30px}
.grey-band{left:0;top:1413px;width:1200px;height:563px;background:linear-gradient(180deg,#e7e7e7 0%,#f3f3f3 40%,#fff 100%)}
.video-frame{left:324px;top:1183px;width:549px;height:340px;background:#fff;border:2px solid #ddd;box-shadow:0 2px 6px rgba(0,0,0,.25);padding:10px}
.video-still{width:100%;height:100%;background:linear-gradient(90deg,#cfcfcf 0%,#c6c6c6 60%,#7d9a6f 62%,#8aa28a 100%)}
.play{left:553px;top:1310px}
.cards{left:0;top:0}
.card{position:absolute;top:1598px;width:240px;text-align:center}
.ring{width:156px;height:156px;margin:0 auto;border:14px solid var(--sky);border-radius:50%;display:flex;align-items:center;justify-content:center}
.card h3{margin-top:34px;font:400 21px "Mulish",sans-serif;color:var(--navy)}
.card p{margin-top:8px;font:400 13px/18px "Open Sans",sans-serif;color:#888}
.card .btn-line{margin:12px auto 0;width:121px;height:34px;border:1px solid #444;font:400 12px "Mulish",sans-serif;display:flex;align-items:center;justify-content:center;color:#222}
.footer{left:0;top:1976px;width:1200px;height:312px;background:var(--footer);color:#fff}
.foot-brand{left:140px;top:2037px;width:220px;text-align:center}
.foot-ring{width:110px;height:110px;border:6px solid #fff;border-radius:50%;margin:0 auto}
.foot-name{font:700 37px/1 "Mulish",sans-serif;margin-top:14px}
.foot-phone{font:400 18px "Mulish",sans-serif;margin-top:4px}
.foot-col h4{font:400 18px "Mulish",sans-serif;letter-spacing:.5px;margin-bottom:14px}
.foot-col li{list-style:none;font:400 14px "Open Sans",sans-serif;height:30px}
.contact-li{display:flex;gap:12px;align-items:flex-start}
.bottombar{left:0;top:2288px;width:1200px;height:62px;background:var(--footer-bottom);text-align:center;font:400 14px/62px "Open Sans",sans-serif;color:#556}
</style>
</head>
<body>
<div class="abs topbar"></div>
<div class="abs client-login">Client Login</div>
<div class="abs social" aria-label="Social links"><span></span><span></span><span></span><span></span></div>

<header class="abs header"></header>
<div class="abs brand">
  <span class="brand-dot"></span>
  <div><div class="brand-name">Fern Porter</div><div class="brand-phone">1-855-Fern KQS</div></div>
</div>
<nav class="nav">
  <a class="active" style="left:448px">Home</a>
  <a style="left:537px">Residents</a>
  <a style="left:663px">Proaperty Management</a>
  <a style="left:913px">About</a>
  <a style="left:1004px">Contact</a>
</nav>
<div class="abs nav-underline"></div>

<section class="abs hero" role="img" aria-label="Marsh landscape with tall grass and winding water under a misty sky"></section>
<h1 class="abs hero-title">Improve the Day with Valet</h1>
<p class="abs hero-sub">Class aptent taciti sociosqu &nbsp;litora torquent</p>
<div class="abs hero-btn">Sign Up Now</div>
<div class="abs dots"><span></span><span></span><span class="on"></span><span></span></div>

<h2 class="abs section-title welcome-title">Welcome to Our Website</h2>
<div class="abs title-rule" style="top:850px"></div>
<div class="abs intro">
  <p>Fern Porter is a leading valet trash and recycling service provider offering robust and flexible solutions for your community’s recycling, waste and maintenance needs.</p>
  <p>Connect with us and let us give you and your residents the experience they deserve: Better people, better processes, and better technologies.</p>
</div>
<div class="abs btn-fill">READ MORE</div>
<div class="abs divider"></div>

<h2 class="abs section-title video-title">Watch Our Video</h2>
<div class="abs title-rule" style="top:1161px"></div>
<div class="abs grey-band"></div>
<div class="abs video-frame"><div class="video-still" role="img" aria-label="Video still: presenter beside an aerial view of an apartment community"></div></div>
<svg class="abs play" width="92" height="92" viewBox="0 0 92 92" aria-label="Play video"><circle cx="46" cy="46" r="46" fill="#fff"/><path d="M37 30 L62 46 L37 62 Z" fill="#111"/></svg>

<div class="card" style="left:80px">
  <div class="ring"><svg width="64" height="64" viewBox="0 0 64 64" fill="var(--navy)"><rect x="8" y="10" width="30" height="48"/><rect x="38" y="26" width="20" height="32"/><g fill="#fff"><rect x="14" y="17" width="7" height="7"/><rect x="25" y="17" width="7" height="7"/><rect x="14" y="30" width="7" height="7"/><rect x="25" y="30" width="7" height="7"/><rect x="18" y="44" width="10" height="14"/><rect x="44" y="33" width="8" height="6"/><rect x="44" y="45" width="8" height="6"/></g></svg></div>
  <h3>Residents</h3><p>Aymenaeos Proin nulla arcu<br>nonummy luctus</p><div class="btn-line">READ MORE</div>
</div>
<div class="card" style="left:331px">
  <div class="ring"><svg width="70" height="64" viewBox="0 0 70 64" fill="var(--navy)"><path d="M20 28 L38 12 L56 28 L56 30 L52 30 L52 44 L24 44 L24 30 L20 30 Z"/><rect x="34" y="30" width="4" height="4" fill="#fff"/><rect x="39" y="30" width="4" height="4" fill="#fff"/><path d="M6 40 L18 40 Q30 48 44 48 L58 44 Q62 46 58 50 L42 58 L16 56 L6 56 Z"/></svg></div>
  <h3>Property Management</h3><p>Aymenaeos Proin nulla arcu<br>nonummy luctus</p><div class="btn-line">READ MORE</div>
</div>
<div class="card" style="left:602px">
  <div class="ring"><svg width="76" height="60" viewBox="0 0 76 60" fill="var(--navy)"><circle cx="38" cy="16" r="10"/><path d="M20 56 Q20 30 38 30 Q56 30 56 56 Z"/><circle cx="16" cy="22" r="8"/><path d="M2 56 Q2 34 16 34 Q24 34 26 40 L22 56 Z"/><circle cx="60" cy="22" r="8"/><path d="M74 56 Q74 34 60 34 Q52 34 50 40 L54 56 Z"/></svg></div>
  <h3>About us</h3><p>Aymenaeos Proin nulla arcu<br>nonummy luctus</p><div class="btn-line">READ MORE</div>
</div>
<div class="card" style="left:864px">
  <div class="ring"><svg width="56" height="56" viewBox="0 0 56 56" fill="none" stroke="var(--navy)" stroke-width="3"><path d="M14 6 L22 16 Q24 19 21 22 L18 25 Q24 36 31 38 L34 35 Q37 32 40 34 L50 42 Q52 45 48 49 Q42 54 34 50 Q14 40 6 22 Q3 14 8 8 Q11 4 14 6 Z"/></svg></div>
  <h3>Contact</h3><p>Aymenaeos Proin nulla arcu<br>nonummy luctus</p><div class="btn-line">READ MORE</div>
</div>

<footer class="abs footer"></footer>
<div class="abs foot-brand">
  <div class="foot-ring"></div>
  <div class="foot-name">Fern Porter</div>
  <div class="foot-phone">1-855-Fern KQS</div>
</div>
<div class="abs foot-col" style="left:428px;top:2041px;color:#fff">
  <h4>QUICK LINKS</h4>
  <ul><li>Home</li><li>About Us</li><li>Residents</li><li>Property Management</li></ul>
</div>
<div class="abs foot-col" style="left:663px;top:2041px;color:#fff">
  <h4>RESOURCES</h4>
  <ul><li>Our Blogs</li><li>Blogs</li><li>Contact Us</li></ul>
</div>
<div class="abs foot-col" style="left:884px;top:2041px;color:#fff">
  <h4>CONTACT INFO</h4>
  <ul>
    <li class="contact-li"><svg width="16" height="20" viewBox="0 0 16 20" fill="#fff"><path d="M8 0 A8 8 0 0 1 16 8 C16 13 8 20 8 20 C8 20 0 13 0 8 A8 8 0 0 1 8 0 Z"/><circle cx="8" cy="8" r="3" fill="var(--footer)"/></svg><span>48 Marsh Reed Lane #4B<br>&nbsp;Texas 75000 TX</span></li>
    <li style="height:30px"></li>
    <li class="contact-li"><svg width="18" height="18" viewBox="0 0 56 56" fill="none" stroke="#fff" stroke-width="4"><path d="M14 6 L22 16 Q24 19 21 22 L18 25 Q24 36 31 38 L34 35 Q37 32 40 34 L50 42 Q52 45 48 49 Q42 54 34 50 Q14 40 6 22 Q3 14 8 8 Q11 4 14 6 Z"/></svg><span>555.010.2468</span></li>
    <li class="contact-li"><svg width="18" height="14" viewBox="0 0 18 14" fill="none" stroke="#fff" stroke-width="1.5"><rect x="1" y="1" width="16" height="12"/><path d="M1 1 L9 8 L17 1"/></svg><span>info@fernporter-example.com</span></li>
  </ul>
</div>
<div class="abs bottombar">© 2017 Company Name &nbsp;All right reserved</div>
</body>
</html>
```